Business card design needed

partition walls
suspended ceilings
bulkheads
shops
office fitouts
compressed sheeting

main colour aqua blue with silver and white writing

k.r.m plastering (vic) pty.ltd

noel carrow
M:0400712864 E:krmplastering@mailvane.com
ABN: 64 203 917 482
ACN: 271 604 815

```html
<!DOCTYPE html>
<html lang="en">
<head>
<meta charset="utf-8">
<title>K.R.M Plastering – Business Card</title>
<link rel="stylesheet" href="https://fonts.googleapis.com/css2?family=Open+Sans:wght@400;700&display=swap">
<style>
  :root {
    --page-bg: #3a3a3a;
    --card-bg: #ffffff;
    --brand-blue: #2e8fdc;
    --deep-blue: #0b3fa8;
    --mid-blue: #1f7fe0;
    --light-blue: #5ec4f2;
    --silver: #dcdcdc;
    --ink: #222222;
  }
  * { margin: 0; padding: 0; box-sizing: border-box; }
  html, body {
    width: 1200px;
    height: 1000px;
    overflow: hidden;
    background: var(--page-bg);
    font-family: "Open Sans", Arial, sans-serif;
  }
  .business-card {
    position: absolute;
    left: 215px;
    top: 280px;
    width: 770px;
    height: 440px;
    background: var(--card-bg);
    overflow: hidden;
  }
  .mosaic-panel {
    position: absolute;
    left: 0;
    top: 0;
    width: 268px;
    height: 440px;
    display: block;
  }
  .company-name {
    position: absolute;
    left: 308px;
    top: 30px;
    font-size: 26px;
    font-weight: 700;
    color: var(--brand-blue);
    letter-spacing: 0.2px;
    white-space: nowrap;
  }
  .contact-block {
    position: absolute;
    left: 392px;
    top: 270px;
  }
  .person-name {
    font-size: 27px;
    font-weight: 700;
    color: var(--brand-blue);
    line-height: 36px;
    white-space: nowrap;
  }
  .contact-list {
    margin-left: 28px;
    margin-top: 4px;
    font-size: 14px;
    line-height: 19.5px;
    color: var(--ink);
  }
  .contact-label { font-weight: 700; }
  .registration {
    position: absolute;
    right: 22px;
    top: 410px;
    font-size: 13.5px;
    color: var(--ink);
    white-space: nowrap;
  }
  .registration span + span { margin-left: 22px; }
  .registration b { font-weight: 700; }
</style>
</head>
<body>
  <main class="business-card">
    <svg class="mosaic-panel" viewBox="0 0 268 440" role="img" aria-label="Decorative blue square-tile mosaic fading into silver tiles">
      <defs>
        <linearGradient id="mosaicVertical" x1="0" y1="0" x2="0" y2="1">
          <stop offset="0" stop-color="#3aa0ea"/>
          <stop offset="0.5" stop-color="#2a8fe6"/>
          <stop offset="1" stop-color="#0b3fa8"/>
        </linearGradient>
        <linearGradient id="mosaicFade" x1="0" y1="0" x2="1" y2="0">
          <stop offset="0" stop-color="#ffffff" stop-opacity="0"/>
          <stop offset="0.72" stop-color="#ffffff" stop-opacity="0"/>
          <stop offset="0.82" stop-color="#e2e2e2" stop-opacity="0.9"/>
          <stop offset="1" stop-color="#ffffff" stop-opacity="1"/>
        </linearGradient>
      </defs>
      <rect width="268" height="440" fill="url(#mosaicVertical)"/>
      <rect width="268" height="440" fill="url(#mosaicFade)"/>
    </svg>

    <h1 class="company-name">K.R.M PLASTERING (VIC) PTY.LTD</h1>

    <section class="contact-block">
      <h2 class="person-name">NOEL CARROW</h2>
      <div class="contact-list">
        <div class="contact-label">Phone:</div>
        <div>0400712864</div>
        <div class="contact-label">Email:</div>
        <div>krmplastering@mailvane.com</div>
      </div>
    </section>

    <footer class="registration">
      <span><b>ABN:</b> 64 203 917 482</span>
      <span><b>ACN:</b> 271 604 815</span>
    </footer>
  </main>
</body>
</html>
```